Property Developer Business card design

we need a business card design + printing for a new Property developer company based in melbourne.
We are a group of investors investing in a property developer business. We have more projects involved in residential property as opposed to commercial property but we are involved in both market. we also provide consulting services with overseas investors willing to invest in the australian property market.
Updates
I have uploaded the logo. I'm not very convince with the colors of my logo... any suggestion please?.
Thanks guys!
Target Market(s)
property investors or person willing to purchase investment property
Industry/Entity Type
Residential
Contact Information for Business Card
Harbourne Capital Australia Pty Ltd
Look and feel
Each slider illustrates characteristics of the customer's brand and the style your logo design should communicate.

```html
<!DOCTYPE html>
<html lang="en">
<head>
<meta charset="utf-8">
<title>Harbourne Capital Australia – Business Card</title>
<link rel="stylesheet" href="https://fonts.googleapis.com/css2?family=Questrial&display=swap">
<style>
  :root {
    --bg: #ecebe8;
    --card: #ffffff;
    --lime: #8fd61a;
    --charcoal: #3a3a3a;
    --brand-blue: #1b8fd6;
    --ink: #333333;
    --muted: #555555;
    --white: #ffffff;
  }
  * { box-sizing: border-box; margin: 0; padding: 0; }
  html, body { width: 1200px; height: 1000px; overflow: hidden; }
  body {
    background: var(--bg);
    font-family: "Questrial", "Century Gothic", sans-serif;
    position: relative;
  }
  .card {
    position: absolute;
    left: 250px;
    width: 700px;
    height: 400px;
    background: var(--card);
    border-radius: 46px 0 46px 0;
    overflow: hidden;
    box-shadow: 0 6px 18px rgba(0,0,0,0.12);
  }
  .card--front { top: 70px; }
  .card--back { top: 530px; }

  /* front */
  .swoosh { position: absolute; inset: 0; width: 700px; height: 400px; }
  .name-tag {
    position: absolute;
    left: 0; top: 150px;
    background: var(--lime);
    color: var(--white);
    font-size: 28px;
    letter-spacing: 1.5px;
    padding: 6px 18px 6px 30px;
  }
  .job-title {
    position: absolute;
    left: 60px; top: 204px;
    font-size: 14px;
    letter-spacing: 1px;
    color: var(--ink);
  }
  .brand {
    position: absolute;
    display: flex;
    align-items: center;
    color: var(--brand-blue);
    white-space: nowrap;
  }
  .brand__mark { background: var(--brand-blue); flex: none; border-radius: 50%; }
  .brand__name { display: flex; flex-direction: column; align-items: center; line-height: 1.15; }

  .card--front .brand { left: 270px; top: 118px; font-size: 25px; gap: 10px; }
  .card--front .brand__mark { width: 16px; height: 16px; }

  .contact {
    position: absolute;
    right: 24px; bottom: 22px;
    list-style: none;
    text-align: right;
    color: var(--white);
    font-size: 13px;
    letter-spacing: 1.4px;
    line-height: 20px;
  }
  .contact li { display: flex; justify-content: flex-end; align-items: center; gap: 8px; }
  .contact svg { width: 13px; height: 13px; flex: none; }

  /* back */
  .accent-left {
    position: absolute; left: 0; top: 200px;
    width: 16px; height: 200px; background: var(--lime);
  }
  .accent-right {
    position: absolute; right: 0; top: 0;
    width: 16px; height: 180px; background: var(--charcoal);
  }
  .card--back .brand {
    left: 0; right: 0; top: 110px;
    justify-content: center;
    font-size: 44px;
    gap: 16px;
  }
  .card--back .brand__mark { width: 26px; height: 26px; }
  .website {
    position: absolute;
    left: 0; right: 0; top: 292px;
    text-align: center;
    font-size: 12px;
    letter-spacing: 7px;
    color: var(--muted);
  }
</style>
</head>
<body>

<section class="card card--front" aria-label="Business card front">
  <svg class="swoosh" viewBox="0 0 700 400" aria-hidden="true">
    <path d="M0,400 C260,330 560,230 700,10 L700,400 Z" fill="var(--lime)"/>
    <path d="M30,400 C300,345 590,250 700,70 L700,400 Z" fill="var(--charcoal)"/>
  </svg>

  <div class="name-tag">Daniel Reyes</div>
  <div class="job-title">Managing Director</div>

  <div class="brand">
    <span class="brand__mark"></span>
    <span class="brand__name"><span>Harbourne Capital</span><span>Australia</span></span>
  </div>

  <ul class="contact">
    <li>0400 555 182
      <svg viewBox="0 0 12 12"><rect x="3" y="0.5" width="6" height="11" rx="1" fill="none" stroke="var(--lime)" stroke-width="1.2"/></svg>
    </li>
    <li>+61 3 9000 4821
      <svg viewBox="0 0 12 12"><path d="M2,1 L4.5,1 L5.5,4 L4,5 C5,7 6,8 7,8 L8,6.5 L11,7.5 L11,10 C6,11 1,6 2,1 Z" fill="var(--lime)"/></svg>
    </li>
    <li>daniel.reyes@harbournecapital.com.au
      <svg viewBox="0 0 12 12"><rect x="0.5" y="2" width="11" height="8" fill="var(--lime)"/><path d="M0.5,2 L6,6.5 L11.5,2" fill="none" stroke="var(--charcoal)" stroke-width="1"/></svg>
    </li>
    <li>www.harbournecapitalaustralia.com.au
      <svg viewBox="0 0 12 12"><path d="M6,0.5 C3.5,0.5 2,2.3 2,4.5 C2,7.5 6,11.5 6,11.5 C6,11.5 10,7.5 10,4.5 C10,2.3 8.5,0.5 6,0.5 Z" fill="var(--lime)"/><circle cx="6" cy="4.5" r="1.5" fill="var(--charcoal)"/></svg>
    </li>
    <li>12 Wattlebird Lane Tarneit VIC 3030
      <svg viewBox="0 0 12 12"><path d="M6,0.5 L11.5,6 L10,6 L10,11.5 L2,11.5 L2,6 L0.5,6 Z" fill="var(--lime)"/></svg>
    </li>
  </ul>
</section>

<section class="card card--back" aria-label="Business card back">
  <div class="accent-right"></div>
  <div class="accent-left"></div>
  <div class="brand">
    <span class="brand__mark"></span>
    <span class="brand__name"><span>Harbourne Capital</span><span>Australia</span></span>
  </div>
  <p class="website">www.harbournecapitalaustralia.com.au</p>
</section>

</body>
</html>
```